Velorin Biotechnology needs a professional powerpoint design

We would like to re-design our powerpoint template(as attachment 1), it should be based on our current logo (as attachment 2). We hope the new powerpoint template could be more professional and like a biotechnology company with advanced technology.
Velorin Biotechnology is a contract development and manufacturing organization to provide high quality services to our clients in development, lead-in advanced technology and cGMP manufacturing of biopharmaceuticals from clinical to commercial manufacturing. We offers the advanced technology and services to become the best partner for clients from clinical to commercial manufacturing.
Reason: We would like to extend the deadline for this project so that designers can have more time to prepare, thanks.
Target Market(s)
Velorin Biotechnology is a contract development and manufacturing organization to provide high quality services to our clients in development, lead-in advanced technology and cGMP manufacturing of biopharmaceuticals from clinical to commercial manufacturing.
Velorin primary focus on development and manufacturing of glycoprotein pharmaceuticals against breast cancer, supplies KEV Taiwan with KEV-347 & KEV-348 for global clinical trials and commercialization in the future. Velorin offers the advanced technology and services to become the best partner for clients from clinical to commercial manufacturing.
Industry/Entity Type
Biotechnology
Requirements
Must have
- The new powerpoint design should based on our current logo.
Should not have
- The similar design with current powerpoint style. Please don't refer the design style of our current website http://www.velorin-example.com.tw/ as well, we will re-design it soon.

```html
<!DOCTYPE html>
<html lang="en">
<head>
<meta charset="utf-8">
<title>Velorin Biotechnology – Slide Template</title>
<link href="https://fonts.googleapis.com/css2?family=Open+Sans:ital,wght@0,400;0,700;1,400;1,600&display=swap" rel="stylesheet">
<style>
  :root {
    --page: #ffffff;
    --ink: #3b3b3b;
    --body: #2a2a2a;
    --green: #7cb342;
    --muted: #777777;
    --shadow: rgba(0, 0, 0, 0.28);
  }
  * { box-sizing: border-box; margin: 0; padding: 0; }
  html, body { width: 1200px; height: 1200px; overflow: hidden; background: var(--page); }
  body { position: relative; font-family: "Open Sans", Arial, sans-serif; color: var(--body); }

  .slide {
    position: absolute; left: 216px; width: 768px; height: 432px;
    background: var(--page);
    box-shadow: 2px 2px 4px var(--shadow);
  }
  .slide--gallery { top: 46px; }
  .slide--features { top: 526px; }

  .slide__accent { position: absolute; left: 32px; top: 50px; width: 6px; height: 46px; background: var(--green); }
  .slide__title {
    position: absolute; left: 48px; top: 44px;
    font-size: 27px; font-style: italic; font-weight: 600; color: var(--ink); letter-spacing: -0.3px;
    white-space: nowrap;
  }
  .slide__subtitle {
    position: absolute; left: 49px; top: 78px;
    font-size: 15px; font-style: italic; font-weight: 600; color: var(--green); white-space: nowrap;
  }

  .brand { position: absolute; right: 32px; top: 46px; display: flex; align-items: center; gap: 6px; }
  .brand__dot { width: 14px; height: 14px; border-radius: 50%; background: var(--green); }
  .brand__name { font-size: 17px; font-weight: 700; color: var(--ink); white-space: nowrap; }

  .photo-strip { position: absolute; left: 0; top: 130px; width: 768px; height: 136px; display: flex; }
  .photo-strip__panel { flex: 1; height: 100%; }
  .photo--globe { background: linear-gradient(120deg, #c9c4bb 0%, #b8bcc4 40%, #2f7fd0 70%, #3d8a3a 100%); }
  .photo--sprout { background: linear-gradient(150deg, #2a5fb8 0%, #6d94cf 45%, #7fae3c 75%, #8a4a2e 100%); }
  .photo--tubes { background: linear-gradient(160deg, #5fbf3a 0%, #e9ece6 35%, #f3eee8 70%, #63d13a 100%); }
  .photo--loupe { background: linear-gradient(140deg, #2d2a26 0%, #3b4a52 45%, #8fa0a8 70%, #eef0f0 100%); }

  .text-column {
    position: absolute; top: 279px; width: 298px;
    font-size: 10px; line-height: 13.4px;
  }
  .text-column--left { left: 39px; }
  .text-column--right { left: 391px; }

  .slide__footer-bar { position: absolute; right: 0; top: 395px; width: 60px; height: 5px; background: var(--green); }
  .slide__number { position: absolute; left: 742px; top: 408px; font-size: 8px; color: var(--muted); }

  .feature { position: absolute; top: 109px; width: 140px; text-align: center; }
  .feature__photo { width: 138px; height: 138px; border-radius: 50%; margin: 0 auto; }
  .feature__heading {
    margin-top: 14px; font-size: 15px; font-style: italic; font-weight: 600; color: var(--green);
  }
  .feature__text { margin-top: 3px; font-size: 8.6px; line-height: 11.5px; }
  .feature--1 { left: 61px; }
  .feature--2 { left: 230px; }
  .feature--3 { left: 400px; }
  .feature--4 { left: 568px; }
</style>
</head>
<body>

<section class="slide slide--gallery">
  <div class="slide__accent"></div>
  <h1 class="slide__title">LOREM IPSUM DOLOR SIT AMET</h1>
  <p class="slide__subtitle">Consetetur sadipscing elitr</p>
  <div class="brand"><span class="brand__dot"></span><span class="brand__name">Velorin Biotech</span></div>

  <div class="photo-strip">
    <div class="photo-strip__panel photo--globe" role="img" aria-label="Businesswoman beside a blue globe covered with trees"></div>
    <div class="photo-strip__panel photo--sprout" role="img" aria-label="Green seedlings in a laboratory with blue light"></div>
    <div class="photo-strip__panel photo--tubes" role="img" aria-label="Gloved hands holding test tubes with green liquid"></div>
    <div class="photo-strip__panel photo--loupe" role="img" aria-label="Magnifying glass over seedlings in dark soil"></div>
  </div>

  <p class="text-column text-column--left">Lorem ipsum dolor sit amet, consetetur sadipscing elitr, sed diam nonumy eirmod tempor invidunt ut labore et dolore magna aliquyam erat, sed diam voluptua. At vero eos et accusam. Lorem ipsum dolor sit amet, consetetur sadipscing elitr, sed diam nonumy eirmod tempor invidunt ut labore et dolore magna aliquyam erat, sed diam voluptua. At vero eos et accusam</p>
  <p class="text-column text-column--right">Lorem ipsum dolor sit amet, consetetur sadipscing elitr, sed diam nonumy eirmod tempor invidunt ut labore et dolore magna aliquyam erat, sed diam voluptua. At vero eos et accusamLorem ipsum dolor sit amet, consetetur sadipscing elitr, sed diam nonumy eirmod tempor invidunt ut labore et dolore magna aliquyam erat, sed diam voluptua. At vero eos et accusam</p>

  <div class="slide__footer-bar"></div>
  <span class="slide__number">3</span>
</section>

<section class="slide slide--features">
  <div class="slide__accent"></div>
  <h1 class="slide__title">LOREM IPSUM DOLOR SIT AMET</h1>
  <p class="slide__subtitle">Consetetur sadipscing elitr</p>
  <div class="brand"><span class="brand__dot"></span><span class="brand__name">Velorin Biotech</span></div>

  <article class="feature feature--1">
    <div class="feature__photo photo--globe" role="img" aria-label="Businesswoman beside a blue globe covered with trees"></div>
    <h2 class="feature__heading">Lorem ipsum</h2>
    <p class="feature__text">Lorem ipsum dolor sit amet, consetetur sadipscing elitr, sed diam nonumy eirmod tempor invidunt ut labore et dolore magna aliquyam erat, sed diam voluptua. At vero eos et accusam et justo duo dolores et ea rebum. Stet clita kasd gubergren, no sea takimata sanctus est</p>
  </article>
  <article class="feature feature--2">
    <div class="feature__photo photo--sprout" role="img" aria-label="Green seedlings in a laboratory with blue light"></div>
    <h2 class="feature__heading">Lorem ipsum</h2>
    <p class="feature__text">Lorem ipsum dolor sit amet, consetetur sadipscing elitr, sed diam nonumy eirmod tempor invidunt ut labore et dolore magna aliquyam erat, sed diam voluptua. At vero eos et accusam et justo duo dolores et ea rebum. Stet clita kasd gubergren, no sea takimata sanctus est</p>
  </article>
  <article class="feature feature--3">
    <div class="feature__photo photo--loupe" role="img" aria-label="Magnifying glass over seedlings in dark soil"></div>
    <h2 class="feature__heading">Lorem ipsum</h2>
    <p class="feature__text">Lorem ipsum dolor sit amet, consetetur sadipscing elitr, sed diam nonumy eirmod tempor invidunt ut labore et dolore magna aliquyam erat, sed diam voluptua. At vero eos et accusam et justo duo dolores et ea rebum. Stet clita kasd gubergren, no sea takimata sanctus est</p>
  </article>
  <article class="feature feature--4">
    <div class="feature__photo photo--tubes" role="img" aria-label="Gloved hands holding test tubes with green liquid"></div>
    <h2 class="feature__heading">Lorem ipsum</h2>
    <p class="feature__text">Lorem ipsum dolor sit amet, consetetur sadipscing elitr, sed diam nonumy eirmod tempor invidunt ut labore et dolore magna aliquyam erat, sed diam voluptua. At vero eos et accusam et justo duo dolores et ea rebum. Stet clita kasd gubergren, no sea takimata sanctus est</p>
  </article>

  <div class="slide__footer-bar"></div>
  <span class="slide__number">4</span>
</section>

</body>
</html>
```